Membership card design for video game arena

I need a two sided design for membership cards for my customers. It needs to have instructions on how to book on one side, and a nice catchy design for the other.

Please pull logo and whatever you desire from the website www.vornik-play.com

Industry/Entity Type

Entertainment

Contact Information for Business Card

The front must say Vornik-Play with the address and whatever design you choose. The back must have the details below

Colors

Designer to choose colors to be used in the design.

Requirements
Must have
• Frontside
• Company name address and phone number
• Backside
• Booking Instructions
• www.Vornik-Play.com/book-now
• Click on General Admission and input information
• Use code Gatepass7 to gain access
• See you there!
Nice to have
• A nice design and whatever you find is pertinent
Should not have
• Useless info

```html
<!DOCTYPE html>
<html lang="en">
<head>
<meta charset="utf-8">
<title>Vornik-Play Membership Card</title>
<link rel="stylesheet" href="https://fonts.googleapis.com/css2?family=Arimo:wght@400;700&display=swap">
<style>
  :root {
    --backdrop: #dcd8d3;
    --navy: #0e2a4d;
    --coral: #e97156;
    --white: #ffffff;
    --highlight: #c4c4c4;
    --ink: #333333;
    --shadow: rgba(0, 0, 0, 0.35);
  }
  * { margin: 0; padding: 0; box-sizing: border-box; }
  html, body {
    width: 1063px;
    height: 1200px;
    overflow: hidden;
    background: var(--backdrop);
    font-family: "Arimo", Arial, sans-serif;
  }
  .card {
    position: absolute;
    left: 100px;
    width: 849px;
    height: 485px;
    color: var(--white);
    box-shadow: 6px 10px 22px var(--shadow);
  }
  .card--front { top: 94px; background: var(--navy); }
  .card--back {
    top: 615px;
    background: linear-gradient(90deg, var(--coral) 0%, #a4575a 30%, #5a3a58 62%, var(--navy) 100%);
  }
  .brand {
    position: absolute;
    left: 0;
    right: 0;
    top: 49px;
    text-align: center;
  }
  .brand__mark {
    display: block;
    width: 94px;
    height: 94px;
    margin: 0 auto;
    border-radius: 50%;
    background: var(--white);
  }
  .brand__name {
    display: block;
    margin-top: 12px;
    font-size: 30px;
    font-weight: 700;
    letter-spacing: 2px;
    text-transform: uppercase;
  }
  .contact {
    position: absolute;
    left: 0;
    right: 0;
    top: 355px;
    text-align: center;
    font-size: 22px;
    letter-spacing: 0.3px;
  }
  .contact__line {
    display: flex;
    justify-content: center;
    align-items: center;
    gap: 14px;
    height: 34px;
  }
  .contact__icon { width: 24px; height: 26px; fill: var(--white); }
  .booking {
    position: absolute;
    left: 0;
    right: 0;
    top: 224px;
    text-align: center;
  }
  .booking__title {
    font-size: 25px;
    text-decoration: underline;
    text-underline-offset: 3px;
    text-decoration-thickness: 1px;
    margin-bottom: 36px;
  }
  .booking__step {
    display: inline-block;
    background: var(--highlight);
    color: var(--ink);
    font-size: 22px;
    line-height: 25px;
    padding: 0 2px;
    margin-bottom: 13px;
  }
  .booking__signoff {
    position: absolute;
    right: 85px;
    top: 433px;
    font-size: 22px;
  }
</style>
</head>
<body>
  <section class="card card--front">
    <div class="brand">
      <span class="brand__mark"></span>
      <span class="brand__name">Vornik-Play</span>
    </div>
    <div class="contact">
      <p class="contact__line">
        <svg class="contact__icon" viewBox="0 0 24 24" aria-hidden="true"><path d="M6.6 10.8a15.1 15.1 0 0 0 6.6 6.6l2.2-2.2a1 1 0 0 1 1-.25 11.4 11.4 0 0 0 3.6.57 1 1 0 0 1 1 1V20a1 1 0 0 1-1 1A17 17 0 0 1 3 4a1 1 0 0 1 1-1h3.5a1 1 0 0 1 1 1c0 1.25.2 2.45.57 3.57a1 1 0 0 1-.25 1z"/></svg>
        555.014.2290
      </p>
      <p class="contact__line">
        <svg class="contact__icon" viewBox="0 0 24 26" aria-hidden="true"><path d="M12 1a7 7 0 0 0-7 7c0 5 7 12 7 12s7-7 7-12a7 7 0 0 0-7-7zm0 9.5A2.5 2.5 0 1 1 12 5.5a2.5 2.5 0 0 1 0 5z"/><path d="M7 18.5c-3 .6-5 1.7-5 3 0 2 4.5 3.5 10 3.5s10-1.5 10-3.5c0-1.3-2-2.4-5-3l-.6 1.2c2.4.5 4 1.2 4 1.8 0 1-3.8 2-8.4 2s-8.4-1-8.4-2c0-.6 1.6-1.3 4-1.8z"/></svg>
        1270 N CALDER AVE, BROOKFIELD FL 33990
      </p>
    </div>
  </section>

  <section class="card card--back">
    <div class="brand">
      <span class="brand__mark"></span>
      <span class="brand__name">Vornik-Play</span>
    </div>
    <div class="booking">
      <h2 class="booking__title" style="font-weight:400">BOOKING INSTRUCTIONS</h2>
      <p><span class="booking__step">WWW.VORNIK-PLAY.COM/BOOK-NOW</span></p>
      <p><span class="booking__step">CLICK ON GENERAL ADMISSION AND INPUT INFORMATION</span></p>
      <p><span class="booking__step">USE CODE GATEPASS7 TO GAIN ACCESS</span></p>
    </div>
    <p class="booking__signoff">SEE YOU THERE!</p>
  </section>
</body>
</html>
```